I need a book cover related to cancer immunotherapy. It is related to cancer immunotherapy, and how patients can enhance their treatment results. It also discusses how adding cryoablation to immunotherapy increases the results as well.
I would like the cover to include a something related to cancer immunotherapy are immunology, such as a T cell, or antibody. I would like it to also include something related to cryoablation of cancer.

Target Market(s)

Cancer Patients and their families

Colors

Designer to choose colors to be used in the design.

Requirements
Must have
• Title is:
• The Quiet Harvest Within
• A Reader's Map Through Healing Waters
• Darren T. Holcombe, MD
Nice to have
• I would like something that relates to immunotherapy (maybe something that looks like an antibody). And also something that relates to cryoablation (freezing of a cancer). You can get a feel for our work on www.holcombeoncocenter.example

```html
<!DOCTYPE html>
<html lang="en">
<head>
<meta charset="utf-8">
<title>The Quiet Harvest Within — Book Cover</title>
<link rel="stylesheet" href="https://fonts.googleapis.com/css2?family=Teko:wght@500;600&family=Cinzel:wght@500&display=swap">
<style>
  :root {
    --paper: #ffffff;
    --paper-shade: #e4e4e4;
    --ink: #141414;
    --accent-red: #e01419;
    --cell-blue: #2a49c4;
    --cell-violet: #6a3aa0;
    --cell-red: #d3202a;
  }
  html, body {
    margin: 0;
    padding: 0;
    width: 800px;
    height: 1200px;
    overflow: hidden;
    background: var(--paper);
  }
  .book-cover {
    display: block;
    width: 800px;
    height: 1200px;
  }
  .title-line {
    font-family: "Teko", "Arial Narrow", sans-serif;
    font-weight: 600;
    fill: var(--ink);
  }
  .title-accent { fill: var(--accent-red); }
  .subtitle {
    font-family: "Cinzel", "Times New Roman", serif;
    font-weight: 500;
    fill: var(--ink);
  }
  .author-name {
    font-family: "Teko", "Arial Narrow", sans-serif;
    font-weight: 500;
    fill: var(--ink);
  }
</style>
</head>
<body>
<svg class="book-cover" viewBox="0 0 800 1200" xmlns="http://www.w3.org/2000/svg">
  <defs>
    <radialGradient id="paperTone" cx="50%" cy="55%" r="65%">
      <stop offset="0%" stop-color="var(--paper-shade)"/>
      <stop offset="60%" stop-color="#f3f3f3"/>
      <stop offset="100%" stop-color="var(--paper)"/>
    </radialGradient>
    <linearGradient id="cellTone" x1="0" y1="0" x2="1" y2="0">
      <stop offset="0%" stop-color="var(--cell-blue)"/>
      <stop offset="55%" stop-color="var(--cell-blue)"/>
      <stop offset="75%" stop-color="var(--cell-violet)"/>
      <stop offset="100%" stop-color="var(--cell-red)"/>
    </linearGradient>
  </defs>

  <rect class="cover-background" width="800" height="1200" fill="url(#paperTone)"/>

  <g class="title-block">
    <text class="title-line" x="92" y="228" font-size="212" textLength="612" lengthAdjust="spacingAndGlyphs">THE <tspan class="title-accent">QUIET</tspan></text>
    <text class="title-line" x="92" y="344" font-size="144" textLength="612" lengthAdjust="spacingAndGlyphs">HARVEST</text>
    <text class="title-line" x="92" y="496" font-size="206" textLength="612" lengthAdjust="spacingAndGlyphs">WITHIN</text>
  </g>

  <g class="subtitle-block">
    <text class="subtitle" x="400" y="570" font-size="36" text-anchor="middle" textLength="430" lengthAdjust="spacingAndGlyphs">A Reader's Map Through</text>
    <text class="subtitle" x="400" y="620" font-size="40" text-anchor="middle" textLength="604" lengthAdjust="spacingAndGlyphs">Healing Waters</text>
  </g>

  <circle class="cover-illustration" cx="400" cy="872" r="164" fill="url(#cellTone)"
          role="img" aria-label="Illustration of an immune T cell shaded from blue to red"/>

  <text class="author-name" x="104" y="1146" font-size="70" textLength="596" lengthAdjust="spacing">DARREN T. HOLCOMBE, MD</text>
</svg>
</body>
</html>
```